Business Card Design Project

We are a distribution company providing goods to Latin America. We sell everything from Medical equipment, generic medicines, to carecliners. The logo that we use is attached. The logo can incorporate different colors other than black for versatility. The company name is Valdoria International Corporation and/or VIC. The card will be printed using 1 or more of the following: Silk mounted and/or embossed. So if the design ideas could be made to incorporate that technique or any other unique techniques, it would be great. The target market is dialysis centers/doctors.

Basic Info for card:
Marnie Dowsett
Purchasing Manager
555-317-4086 direct
555-241-7953 fax
marnie.dowsett@valdoriavic.example
www.valdoriavic.example

Target Market(s)

Latin America

Industry/Entity Type

Business

Requirements
Nice to have
• The Front of the card should have the basic contact information with company name/logo. The back of the card could incorporate

```html
<!DOCTYPE html>
<html lang="en">
<head>
<meta charset="utf-8">
<title>Valdoria International Corporation – Business Cards</title>
<link href="https://fonts.googleapis.com/css2?family=Source+Sans+3:wght@400;600&family=Arimo:wght@700&display=swap" rel="stylesheet">
<style>
  :root {
    --page: #ecebe8;
    --card: #ffffff;
    --ink: #1c1c1c;
    --accent: #e2573b;
    --muted: #a3a3a3;
    --stripe: #f3c98a;
    --shadow: rgba(0,0,0,0.18);
  }
  html, body {
    margin: 0;
    width: 1200px;
    height: 741px;
    overflow: hidden;
    background: var(--page);
    font-family: "Source Sans 3", sans-serif;
  }
  .stage {
    position: relative;
    width: 1200px;
    height: 741px;
  }
  .card {
    position: absolute;
    top: 222px;
    width: 520px;
    height: 297px;
    background: var(--card);
    box-shadow: 0 6px 18px var(--shadow);
    overflow: hidden;
  }
  .card--front { left: 50px; }
  .card--back { left: 630px; }

  /* Front */
  .front-lines {
    position: absolute;
    right: 0;
    bottom: 0;
    width: 520px;
    height: 297px;
  }
  .brand {
    position: absolute;
    left: 26px;
    top: 30px;
    display: flex;
    align-items: center;
    gap: 12px;
  }
  .brand-mark {
    width: 34px;
    height: 34px;
    border-radius: 50%;
    background: var(--ink);
    flex: none;
  }
  .brand-name {
    font-size: 25px;
    line-height: 1.02;
    font-weight: 400;
    color: var(--ink);
  }
  .person {
    position: absolute;
    left: 26px;
    top: 120px;
  }
  .person-name {
    font-size: 26px;
    color: var(--accent);
    margin: 0;
    font-weight: 400;
    line-height: 1;
  }
  .person-title {
    font-size: 12px;
    color: var(--muted);
    margin: 3px 0 14px;
  }
  .contact {
    list-style: none;
    margin: 0;
    padding: 0;
    font-size: 12.5px;
    color: var(--ink);
  }
  .contact li {
    display: flex;
    align-items: center;
    gap: 8px;
    height: 17px;
  }
  .contact-tag {
    width: 11px;
    height: 11px;
    background: var(--accent);
    color: #fff;
    font-size: 8px;
    line-height: 11px;
    text-align: center;
    font-weight: 600;
  }

  /* Back */
  .back-stripes {
    position: absolute;
    inset: 0;
  }
  .back-mark {
    position: absolute;
    left: 50%;
    top: 36px;
    width: 130px;
    height: 130px;
    margin-left: -65px;
    border-radius: 50%;
    background: var(--ink);
  }
  .back-name {
    position: absolute;
    left: 0;
    right: 0;
    top: 186px;
    text-align: center;
    font-family: "Arimo", sans-serif;
    font-weight: 700;
    font-size: 25px;
    color: var(--ink);
    margin: 0;
  }
  .back-url {
    position: absolute;
    left: 0;
    right: 0;
    top: 248px;
    text-align: center;
    font-size: 12px;
    color: var(--ink);
  }
</style>
</head>
<body>
<main class="stage">

  <section class="card card--front" aria-label="Card front">
    <svg class="front-lines" viewBox="0 0 520 297" aria-hidden="true">
      <g stroke="var(--accent)" stroke-width="1.6">
        <line x1="440" y1="96" x2="520" y2="96"/>
        <line x1="400" y1="112" x2="520" y2="112"/>
        <line x1="360" y1="128" x2="520" y2="128"/>
        <line x1="320" y1="144" x2="520" y2="144"/>
        <line x1="280" y1="160" x2="520" y2="160"/>
        <line x1="260" y1="176" x2="520" y2="176"/>
        <line x1="250" y1="192" x2="520" y2="192"/>
        <line x1="240" y1="208" x2="520" y2="208"/>
        <line x1="230" y1="224" x2="520" y2="224"/>
        <line x1="220" y1="240" x2="520" y2="240"/>
        <line x1="210" y1="256" x2="520" y2="256"/>
        <line x1="0" y1="272" x2="520" y2="272"/>
      </g>
    </svg>

    <div class="brand">
      <span class="brand-mark"></span>
      <span class="brand-name">Valdoria International<br>Corporation</span>
    </div>

    <div class="person">
      <h1 class="person-name">Marnie Dowsett</h1>
      <p class="person-title">Purchasing Manager</p>
      <ul class="contact">
        <li><span class="contact-tag">p</span>555-317-4086</li>
        <li><span class="contact-tag">f</span>555-241-7953</li>
        <li><span class="contact-tag">e</span>marnie.dowsett@valdoriavic.example</li>
        <li><span class="contact-tag">w</span>www.valdoriavic.example</li>
      </ul>
    </div>
  </section>

  <section class="card card--back" aria-label="Card back">
    <svg class="back-stripes" viewBox="0 0 520 297" aria-hidden="true">
      <g stroke="var(--stripe)" stroke-width="1.6">
        <line x1="-280" y1="297" x2="20" y2="0"/>
        <line x1="-250" y1="297" x2="50" y2="0"/>
        <line x1="-220" y1="297" x2="80" y2="0"/>
        <line x1="-190" y1="297" x2="110" y2="0"/>
        <line x1="-160" y1="297" x2="140" y2="0"/>
        <line x1="-130" y1="297" x2="170" y2="0"/>
        <line x1="-100" y1="297" x2="200" y2="0"/>
        <line x1="-70" y1="297" x2="230" y2="0"/>
        <line x1="-40" y1="297" x2="260" y2="0"/>
        <line x1="-10" y1="297" x2="290" y2="0"/>
        <line x1="20" y1="297" x2="320" y2="0"/>
        <line x1="50" y1="297" x2="350" y2="0"/>
        <line x1="80" y1="297" x2="380" y2="0"/>
        <line x1="110" y1="297" x2="410" y2="0"/>
        <line x1="140" y1="297" x2="440" y2="0"/>
        <line x1="170" y1="297" x2="470" y2="0"/>
        <line x1="200" y1="297" x2="500" y2="0"/>
        <line x1="230" y1="297" x2="530" y2="0"/>
        <line x1="260" y1="297" x2="560" y2="0"/>
        <line x1="290" y1="297" x2="590" y2="0"/>
        <line x1="320" y1="297" x2="620" y2="0"/>
        <line x1="350" y1="297" x2="650" y2="0"/>
        <line x1="380" y1="297" x2="680" y2="0"/>
        <line x1="410" y1="297" x2="710" y2="0"/>
        <line x1="440" y1="297" x2="740" y2="0"/>
        <line x1="470" y1="297" x2="770" y2="0"/>
        <line x1="500" y1="297" x2="800" y2="0"/>
      </g>
    </svg>
    <span class="back-mark"></span>
    <h2 class="back-name">Valdoria International Corporation</h2>
    <p class="back-url">www.valdoriavic.example</p>
  </section>

</main>
</body>
</html>
```